Brickpaving & Landscaping flyers

I AM LOOKING FOR FLYERS TO PROMOTE MY BUSINESS. BUSINESS DETAILS ARE AS FOLLOWS
GUS ORCHID YARDWORKS
Your local tradesman.
Brick Paving, Pool Capping, Limestone Retaining, Natural & Synthetic Turf, Garden Bed Edging, Pool Fence Footings, Soakwells. Most suburbs North of the river

gusbellam71@mailvine.example 0418827346
Free no obligation quotes
Fully insured and all work guaranteed!
You can find examples of my work and heaps of reviews at www.socialhub.example/orchidyardworks
Corwin/Tallora based
Discounts offered for all local work

Target Market(s)

Home owners

Industry/Entity Type

Business

Font styles to use
Serif

Colors
ec1f27
fbed22
add136

Requirements
Must have
• Colour, Some green and yellow to represent grass and sand (basic links to landscaping)
Nice to have
• A brick pattern design
Should not have
• Shouldnt be too busy

```html
<!DOCTYPE html>
<html lang="en">
<head>
<meta charset="utf-8">
<title>Gus Orchid Yardworks – Flyer</title>
<link rel="stylesheet" href="https://fonts.googleapis.com/css2?family=Luckiest+Guy&family=Open+Sans:ital,wght@0,600;0,700;0,800;1,700&display=swap">
<style>
  :root {
    --page-bg: #ffffff;
    --sky-top: #8fcbf0;
    --sky-mid: #cfe8f8;
    --sky-light: #eef6fc;
    --brand-blue: #1ea4e9;
    --brand-orange: #f47b2a;
    --ink: #1f1f1f;
    --grass-dark: #3f8a1e;
    --grass-light: #8ccf3a;
    --paving: #8d8a88;
    --paving-light: #c9c6c3;
    --badge-green: #1f9a4a;
    --white: #ffffff;
  }
  * { box-sizing: border-box; margin: 0; padding: 0; }
  html, body { width: 1200px; height: 998px; overflow: hidden; background: var(--page-bg); }
  .flyer {
    position: absolute; left: 267px; top: 30px; width: 665px; height: 942px; overflow: hidden;
    background: linear-gradient(160deg, var(--sky-top) 0%, var(--sky-mid) 30%, var(--sky-light) 50%, var(--sky-mid) 70%);
    font-family: "Open Sans", Arial, sans-serif;
  }
  .grass-photo {
    position: absolute; left: 0; top: 470px; width: 665px; height: 472px;
    background: linear-gradient(180deg, rgba(140,207,58,0) 0%, rgba(140,207,58,.55) 22%, var(--grass-light) 40%, var(--grass-dark) 100%);
  }
  .paving-photo {
    position: absolute; left: 0; top: 620px; width: 665px; height: 322px;
    background: linear-gradient(150deg, var(--paving) 0%, var(--paving-light) 70%);
    clip-path: polygon(0 45%, 55% 12%, 62% 0, 100% 88%, 100% 100%, 0 100%);
  }
  .corner-tab { position: absolute; left: 0; top: 0; }
  .title {
    position: absolute; left: 10px; top: 12px; width: 660px;
    font-family: "Luckiest Guy", Impact, sans-serif; color: var(--brand-blue);
    font-size: 86px; line-height: 74px; text-align: center;
    transform: rotate(-4deg); transform-origin: center;
  }
  .tagline {
    position: absolute; left: 130px; top: 172px; width: 530px;
    font-family: "Luckiest Guy", Impact, sans-serif; color: var(--brand-orange);
    font-size: 37px; letter-spacing: 1px; text-align: center;
    transform: rotate(-4deg);
  }
  .services { position: absolute; list-style: none; font-style: italic; font-weight: 700; font-size: 21px; color: var(--ink); }
  .services li { position: relative; padding-left: 24px; line-height: 24px; margin-bottom: 13px; }
  .services li::before {
    content: ""; position: absolute; left: 2px; top: 5px; width: 9px; height: 9px;
    border-right: 5px solid var(--brand-orange); border-bottom: 5px solid var(--brand-orange);
    transform: rotate(-45deg);
  }
  .services--left { left: 28px; top: 224px; }
  .services--right { left: 343px; top: 221px; }
  .promise {
    position: absolute; width: 206px; height: 206px; border-radius: 50%;
    border: 2px solid var(--brand-orange); background: rgba(255,255,255,.72);
    display: flex; flex-direction: column; align-items: center; justify-content: center;
    font-family: "Luckiest Guy", Impact, sans-serif; color: var(--brand-blue);
    font-size: 23px; line-height: 22px; text-align: center; transform: rotate(-5deg);
  }
  .promise--quotes { left: 8px; top: 417px; }
  .promise--insured { left: 230px; top: 412px; }
  .promise--local { left: 452px; top: 412px; }
  .promise .gap { height: 16px; }
  .promise .small { font-family: "Open Sans", Arial, sans-serif; font-weight: 600; font-size: 17px; line-height: 20px; }
  .contact-box {
    position: absolute; left: 0; top: 634px; width: 331px; height: 121px;
    background: var(--brand-orange); border-top-right-radius: 12px; color: var(--white);
    padding: 18px 0 0 30px;
  }
  .contact-box .phone { font-weight: 800; font-size: 36px; letter-spacing: 1px; line-height: 46px; }
  .contact-box .email { font-weight: 600; font-size: 15px; margin-top: 10px; }
  .contact-badge { position: absolute; left: 294px; top: 716px; }
  .reviews { position: absolute; left: 30px; top: 778px; color: var(--white); }
  .reviews p { font-weight: 600; font-size: 16px; line-height: 24px; }
  .reviews .url { font-weight: 700; font-size: 23px; margin-top: 8px; line-height: 30px; }
  .footer-band {
    position: absolute; left: 0; top: 875px; width: 665px; height: 67px;
    background: rgba(255,255,255,.55); display: flex; align-items: center; padding-left: 30px; gap: 10px;
  }
  .footer-band .mark { width: 40px; height: 40px; border-radius: 50%; background: var(--grass-dark); }
  .footer-band .name { font-weight: 700; font-size: 18px; color: var(--grass-dark); }
</style>
</head>
<body>
<main class="flyer">
  <div class="grass-photo" role="img" aria-label="Close-up photo of green grass blades against the sky"></div>
  <div class="paving-photo" role="img" aria-label="Photo of grey brick paving laid diagonally"></div>

  <svg class="corner-tab" width="80" height="72" viewBox="0 0 80 72" aria-hidden="true">
    <polygon points="0,0 74,0 60,66 0,72" fill="var(--brand-orange)"/>
  </svg>

  <h1 class="title">GUS ORCHID<br>YARDWORKS</h1>
  <p class="tagline">YOUR LOCAL TRADESMAN</p>

  <ul class="services services--left">
    <li>Brick Paving</li>
    <li>Pool Capping</li>
    <li>Limestone Retaining</li>
    <li>Natural &amp; Synthetic Turf</li>
    <li>Garden Bed Edging</li>
  </ul>
  <ul class="services services--right">
    <li>Pool Fence Footings</li>
    <li>Soakwells</li>
    <li>Most suburbs North<br>of the river</li>
  </ul>

  <div class="promise promise--quotes">FREE<br>NO<br>OBLIGATION<br>QUOTES</div>
  <div class="promise promise--insured">FULLY<br>INSURED<div class="gap"></div>ALL WORK<br>GUARANTEED!</div>
  <div class="promise promise--local"><span class="small">CORWIN<br>/TALLORA<br>BASED</span>DISCOUNTS<br>OFFERED FOR<br>ALL LOCAL<br>WORK</div>

  <section class="contact-box">
    <p class="phone">0418 827 346</p>
    <p class="email">gusbellam71@mailvine.example</p>
  </section>
  <svg class="contact-badge" width="60" height="60" viewBox="0 0 60 60" aria-hidden="true">
    <circle cx="30" cy="30" r="27" fill="var(--badge-green)" stroke="var(--white)" stroke-width="4"/>
  </svg>

  <section class="reviews">
    <p>View examples of my work<br>and heaps of reviews at</p>
    <p class="url">www.socialhub.example/orchidyardworks</p>
  </section>

  <footer class="footer-band">
    <span class="mark"></span>
    <span class="name">Gus Orchid Yardworks</span>
  </footer>
</main>
</body>
</html>
```